serious, thorough, light and simple - that's my advice and mediations

My business card should combine my logo (uploaded file) and my homepage (https://fellor-mediation.webnestsite.com).

Contact Information for Business Card

Name: Sabine Fellor di Vanti
Phone: 076 412 58 94
mail: sfellor@postkiv.ch
web: www.fellor-di-vanti.ch

```html
<!DOCTYPE html>
<html lang="de">
<head>
<meta charset="utf-8">
<title>Sabine Fellor di Vanti – Visitenkarte</title>
<link rel="stylesheet" href="https://fonts.googleapis.com/css2?family=Roboto:wght@300;400;500&display=swap">
<style>
  :root {
    --page-bg: #e4e4e2;
    --card-white: #ffffff;
    --gold: #a8844a;
    --green: #1f7345;
    --green-text: #2a6a3f;
    --grad-top: #176b45;
    --grad-bottom: #233f86;
    --white: #ffffff;
  }
  * { box-sizing: border-box; margin: 0; padding: 0; }
  html, body {
    width: 1125px; height: 1200px; overflow: hidden;
    background: var(--page-bg);
    font-family: "Roboto", Arial, sans-serif;
  }
  .card {
    position: absolute; left: 150px; width: 826px; height: 470px;
    border-radius: 24px; overflow: hidden;
  }
  .card--front { top: 98px; background: var(--card-white); }
  .card--back {
    top: 630px;
    background: linear-gradient(to bottom, var(--grad-top), var(--grad-bottom));
  }

  .brand {
    position: absolute; display: flex; flex-direction: column; align-items: center;
  }
  .brand__row { display: flex; align-items: center; gap: 14px; }
  .brand__dot { border-radius: 50%; flex: none; }
  .brand__name { font-weight: 400; white-space: nowrap; }
  .brand__tagline { letter-spacing: 0.32em; text-transform: uppercase; font-weight: 400; white-space: nowrap; }

  .card--front .brand { right: 58px; top: 122px; }
  .card--front .brand__dot { width: 22px; height: 22px; background: var(--gold); }
  .card--front .brand__name { font-size: 44px; color: var(--gold); }
  .card--front .brand__tagline { font-size: 11px; color: var(--green); margin-top: 16px; }

  .holder {
    position: absolute; left: 56px; top: 262px;
    font-size: 28px; font-weight: 500; color: var(--gold);
  }
  .divider {
    position: absolute; left: 56px; right: 56px; top: 314px;
    height: 2px; background: var(--green);
  }
  .contacts {
    position: absolute; left: 56px; top: 332px; list-style: none;
  }
  .contacts li {
    display: flex; align-items: center; gap: 13px;
    height: 33px; font-size: 21px; color: var(--green-text); font-weight: 400;
  }
  .contacts svg { width: 18px; height: 18px; flex: none; }
  .contacts .accent { color: var(--gold); }

  .card--back .brand { left: 0; right: 0; top: 176px; }
  .card--back .brand__dot { width: 30px; height: 30px; background: var(--white); }
  .card--back .brand__name { font-size: 68px; color: var(--white); font-weight: 300; }
  .card--back .brand__tagline { font-size: 14px; color: var(--white); margin-top: 34px; }
  .back__web {
    position: absolute; left: 0; right: 0; top: 410px; text-align: center;
    font-size: 21px; font-weight: 300; color: var(--white);
  }
</style>
</head>
<body>
  <section class="card card--front">
    <div class="brand">
      <div class="brand__row">
        <span class="brand__dot"></span>
        <span class="brand__name">Wege im Dialog</span>
      </div>
      <span class="brand__tagline">Zuhören, Ordnen, Lösen</span>
    </div>

    <h1 class="holder">Sabine Fellor di Vanti</h1>
    <div class="divider"></div>

    <ul class="contacts">
      <li>
        <svg viewBox="0 0 24 24" aria-hidden="true"><path fill="#a8844a" d="M6.6 10.8a15.1 15.1 0 0 0 6.6 6.6l2.2-2.2c.3-.3.7-.4 1-.2 1.1.4 2.3.6 3.6.6.6 0 1 .4 1 1V20c0 .6-.4 1-1 1A17 17 0 0 1 3 4c0-.6.4-1 1-1h3.5c.6 0 1 .4 1 1 0 1.3.2 2.5.6 3.6.1.3 0 .7-.2 1z"/></svg>
        <span>076 412 58 94</span>
      </li>
      <li>
        <svg viewBox="0 0 24 24" aria-hidden="true" fill="none" stroke="#a8844a" stroke-width="2"><rect x="3" y="6" width="18" height="13" rx="1.5"/><path d="M3.5 7l8.5 6.5L20.5 7"/></svg>
        <span>sfellor@postkiv.ch</span>
      </li>
      <li>
        <svg viewBox="0 0 24 24" aria-hidden="true" fill="none" stroke="#a8844a" stroke-width="1.8"><circle cx="12" cy="12" r="9"/><ellipse cx="12" cy="12" rx="4" ry="9"/><path d="M3 12h18M4.5 7.5h15M4.5 16.5h15"/></svg>
        <span>www.<span class="accent">fellor-di-vanti</span>.ch</span>
      </li>
    </ul>
  </section>

  <section class="card card--back">
    <div class="brand">
      <div class="brand__row">
        <span class="brand__dot"></span>
        <span class="brand__name">Wege im Dialog</span>
      </div>
      <span class="brand__tagline">Zuhören, Ordnen, Lösen</span>
    </div>
    <p class="back__web">www.fellor-di-vanti.ch</p>
  </section>
</body>
</html>
```